Template design for organic gardening site for ShopVantra platform

We need a template design for our new 'Fen Leaf Naturals' shopvantra site. Fen Leaf Naturals specialises in organic nutrients for gardening plus all equipment needed to grow.
Domain name will be www.fenleafnaturals.co.uk
Colours used should include logo colours, see attached image. Other colours to compliment the greens and lift the feel of the site could be yellow or orange.
Home page design should include, but not limited to the following:
Interactive banner carousel space
A smaller banner advertising space
Featured products
New products
Sale products feature/link
Articles links/feature
+ all standard shopvantra features such as menus, etc
The site will be selling products (these are nutrients) such as:
Pelvarimost
Marsh hare soil tonic
Terrawix
Nuro pods
Stem triumph
Sprout charm
Vel
Flint amber
Moswelder
+ more products and brands
Site layouts we like include:
www.tidemarkaquafarm.co.uk ... A bit old fashioned but cool
www.lanternbeds.co.uk ... Nice but too compact
www.flintamber.com ... Has a nice top half
www.sponsorapod.org.uk ... Nice colours and header
www.penhurstplants.co.uk ... nice layout, but needs image carousel
www.wrenmeal.co.uk ... Nice background and colours
www.thistle.co.uk ... Nice colours and layout
www.danielmorrowhorticulture.com ... Nice layout and header
www.sprivant.co.uk ... Cool colours and shop pages layout is nice
www.aquavenor.co.uk ... One of the best layouts
The site should feel clean, modern and elegant.
Target Market(s)
Indoor and outdoor organic gardeners
Look and feel

```html
<!DOCTYPE html>
<html lang="en">
<head>
<meta charset="utf-8">
<title>Fen Leaf Naturals – Home</title>
<link rel="stylesheet" href="https://fonts.googleapis.com/css2?family=Open+Sans:wght@400;600;700;800&display=swap">
<style>
:root{
  --green:#52a91d;
  --green-dark:#3f8c12;
  --ink:#333;
  --muted:#8a8a8a;
  --line:#e4e4e4;
  --band:#f2f2f2;
  --foot:#f5f5f5;
  --name:#1f4f9c;
  --star:#f4c20d;
  --sale:#e53935;
  --new:#2f7fd1;
  --dark:#3a3a3a;
}
*{box-sizing:border-box;margin:0;padding:0}
html,body{width:1200px;height:3600px;overflow:hidden;background:#fff}
body{font-family:"Open Sans",Arial,sans-serif;color:var(--ink);font-size:13px;position:relative}
a{color:inherit;text-decoration:none}
.abs{position:absolute}

/* top bar */
.topbar{left:0;top:0;width:1200px;height:40px;background:#f7f7f7;border-bottom:1px solid var(--line);font-size:11px;color:#666}
.topbar .left{left:125px;top:12px;display:flex}
.topbar .right{right:90px;top:12px;display:flex}
.topbar span{padding:0 12px;border-right:1px solid #ddd}
.topbar span:first-child{padding-left:0}
.topbar span:last-child{border-right:0}

/* header */
.logo{left:125px;top:136px;display:flex;align-items:center;gap:10px}
.logo .mark{width:46px;height:46px;background:var(--green);border-radius:4px}
.logo .name{font-weight:800;color:var(--green);font-size:25px;line-height:25px;text-transform:uppercase;width:170px}
.contact{left:365px;top:128px;display:flex;gap:26px;font-size:11px;color:#666;align-items:center}
.contact svg{vertical-align:middle;margin-right:6px}
.search{left:365px;top:152px;width:505px;height:44px;border:2px solid var(--green);display:flex}
.search .field{flex:1;padding:12px 14px;color:#aaa;font-size:12px}
.search .cat{width:145px;border-left:1px solid var(--line);padding:12px;color:#666;font-size:12px;display:flex;justify-content:space-between}
.search .go{width:44px;background:var(--green);display:flex;align-items:center;justify-content:center}
.minis{left:900px;top:160px;font-size:11px;color:#777;line-height:22px}
.minis svg{vertical-align:middle;margin-right:6px}
.cart{left:1010px;top:158px;display:flex;gap:10px;align-items:center}
.cart .label{font-size:11px;color:#777;line-height:14px}
.cart .label b{display:block;color:var(--green);font-size:20px;line-height:24px}
.rule{left:0;width:1200px;height:1px;background:var(--line)}

/* departments */
.depts{left:125px;top:266px;width:228px;height:414px;border:1px solid var(--line);background:#fff}
.depts h3{background:var(--green);color:#fff;font-size:13px;font-weight:700;height:48px;display:flex;align-items:center;padding-left:16px;gap:10px}
.depts li{list-style:none;font-size:12px;color:#555;padding:0 16px;height:35px;line-height:35px;border-bottom:1px solid #f0f0f0}

/* hero */
.hero{left:377px;top:266px;width:734px;height:444px;background:#f1f1f1}
.hero .kicker{position:absolute;left:78px;top:70px;font-size:34px;color:#444;line-height:40px}
.hero .pct{position:absolute;left:78px;top:126px;font-size:62px;color:#444;line-height:70px}
.hero .disc{position:absolute;left:78px;top:196px;font-size:38px;color:#444;line-height:44px}
.hero .sub{position:absolute;left:78px;top:240px;font-size:20px;color:#555;letter-spacing:1px}
.hero .terms{position:absolute;left:78px;top:306px;font-size:12px;color:#555}
.hero .btn{position:absolute;left:78px;top:332px;width:122px;height:42px;background:var(--green);color:#fff;font-weight:700;font-size:12px;display:flex;align-items:center;justify-content:center}
.hero .pack{position:absolute;left:450px;top:30px;width:250px;height:320px;background:linear-gradient(160deg,#e9efe3,#c9c4b3 60%,#8c8a80);border-radius:6px}
.hero .arrow{position:absolute;top:198px;width:26px;height:36px;background:#e4e4e4;display:flex;align-items:center;justify-content:center}
.hero .dots{position:absolute;left:320px;top:418px;display:flex;gap:10px}
.hero .dots i{width:10px;height:10px;border-radius:50%;background:#cfcfcf}
.hero .dots i.is-active{background:var(--green)}

/* promo banners */
.promo{top:734px;width:482px;height:132px;position:absolute;background:linear-gradient(90deg,#eef2f6,#d7dee6)}
.promo .art{position:absolute;top:0;height:132px;width:230px}
.promo h4{position:absolute;font-size:30px;font-weight:700;color:#3c4a5a;font-style:italic}
.promo p{position:absolute;font-size:13px;color:#6a7480}

/* tabs + cards */
.tabs{left:125px;top:912px;display:flex;gap:4px}
.tabs span{height:48px;padding:0 34px;display:flex;align-items:center;font-size:12px;color:#666;border:1px solid var(--line);border-bottom:0;background:#fafafa}
.tabs span.active{background:var(--green);color:#fff;font-weight:700;padding:0 42px}
.row{position:absolute;display:flex;border:1px solid var(--line);background:#fff}
.card{position:relative;border-right:1px solid var(--line);padding:18px 22px 0}
.card:last-child{border-right:0}
.badges{position:absolute;left:0;top:0;display:flex;flex-direction:column;gap:2px}
.badge{font-size:9px;color:#fff;font-weight:700;padding:3px 10px 3px 7px;clip-path:polygon(0 0,100% 0,88% 100%,0 100%)}
.badge.sale{background:var(--sale)}
.badge.best{background:var(--green);padding-right:14px}
.badge.new{background:var(--new)}
.thumb{margin:0 auto;border-radius:4px}
.pname{display:block;color:var(--name);font-weight:700;font-size:12px;margin-top:16px}
.brand{font-size:10px;color:#888;margin-top:3px}
.stars{font-size:11px;color:var(--star);letter-spacing:1px;margin-top:2px}
.stars i{font-style:normal;color:#ccc}
.price{display:flex;justify-content:space-between;align-items:center;margin-top:30px;border-top:1px solid #f0f0f0;padding-top:8px}
.price s{color:#aaa;font-size:11px}
.price b{color:#333;font-size:15px;margin-left:auto}
.addcart{margin:10px auto 0;width:130px;height:36px;background:var(--green);color:#fff;font-weight:700;font-size:12px;display:flex;align-items:center;justify-content:center}
.acts{display:flex;justify-content:center;gap:18px;font-size:10px;color:#999;margin-top:10px}

/* section heads */
.band{left:0;width:1200px;background:var(--band)}
.sec-title{font-size:26px;color:#333;font-weight:400}
.sec-line{height:1px;background:var(--line)}

.grid{left:125px;top:1462px;width:986px;height:510px;background:#fff;border:1px solid var(--line);display:grid;grid-template-columns:192px 192px 192px 410px}
.grid .cell{position:relative;border-right:1px solid var(--line);border-bottom:1px solid var(--line);padding:14px 16px 0;height:254px}
.grid .cell .price{margin-top:14px;border-top:0}
.grid .big{grid-column:4;grid-row:1 / span 2;border-bottom:0;border-right:0;padding:20px 22px;height:508px}

.rv{left:125px;top:2130px;width:986px;height:236px}
.rv .card{width:164px;padding:14px 10px 0;text-align:center}
.rv .pname{font-size:11px;margin-top:10px}
.rv .price{margin-top:10px;border-top:0}

.brands{left:125px;top:2477px;width:986px;display:flex;justify-content:space-between}
.brands div{width:140px;height:70px;border:1px solid var(--line);display:flex;align-items:center;justify-content:center;gap:6px;font-size:13px;color:#555;font-weight:600}
.brands div i{width:14px;height:14px;background:#777}

.navarrows{font-size:16px;color:#aaa;letter-spacing:8px}

/* footer */
.footer{left:0;top:2616px;width:1200px;height:864px;background:var(--foot)}
.fcol{position:absolute;top:52px;width:300px}
.fcol h5{font-size:15px;color:var(--green);font-weight:700;margin-bottom:20px}
.mini{display:flex;justify-content:space-between;height:72px}
.mini .pname{margin-top:0;font-size:11px}
.mini .stars{font-size:10px}
.mini .p{font-size:11px;color:#333;margin-top:4px}
.mini .p s{color:#aaa;margin-right:6px}
.mini .thumb{width:54px;height:54px;margin:0}
.news{left:295px;top:374px;width:645px;height:48px;display:flex}
.news .f{flex:1;background:#fff;border:1px solid var(--line);padding:15px 16px;font-size:11px;color:#aaa}
.news .b{width:116px;background:var(--green);color:#fff;font-weight:700;font-size:12px;display:flex;align-items:center;justify-content:center}
.flogo{left:125px;top:478px;display:flex;align-items:center;gap:10px}
.flogo .mark{width:50px;height:50px;background:var(--green);border-radius:4px}
.flogo .name{font-weight:800;color:var(--green);font-size:26px;line-height:26px;text-transform:uppercase;width:180px}
.about{left:125px;top:556px;width:270px;font-size:12px;line-height:20px;color:#444}
.about b{font-weight:700}
.about p{margin-bottom:22px;color:#777}
.social{display:flex;gap:8px;margin-top:8px}
.social i{width:24px;height:24px;border-radius:50%;background:#333}
.links{position:absolute;top:488px;font-size:12px;color:#999;line-height:25px}
.links h6{font-size:12px;color:#555;font-weight:600;text-transform:uppercase;margin-bottom:12px}
.bottom{left:0;top:3480px;width:1200px;height:58px;background:var(--dark);color:#aaa;font-size:11px}
.bottom .txt{position:absolute;left:125px;top:21px}
.bottom .txt b{color:var(--green)}
.pay{position:absolute;right:90px;top:17px;display:flex;gap:6px}
.pay i{width:44px;height:26px;background:#f2f2f2;border-radius:3px}
</style>
</head>
<body>

<div class="abs topbar">
  <div class="abs left"><span>Home</span><span>Contact Us</span><span>My Account</span></div>
  <div class="abs right"><span>English ▾</span><span>US Dollar (USD) ▾</span><span>Register</span><span>Login</span></div>
</div>

<header>
  <div class="abs logo"><div class="mark"></div><div class="name">Fen Leaf Naturals</div></div>
  <div class="abs contact">
    <span><svg width="14" height="14" viewBox="0 0 24 24"><path fill="#52a91d" d="M6.6 10.8a15 15 0 0 0 6.6 6.6l2.2-2.2c.3-.3.7-.4 1-.2 1.1.4 2.3.6 3.6.6.6 0 1 .4 1 1V20c0 .6-.4 1-1 1A17 17 0 0 1 3 4c0-.6.4-1 1-1h3.5c.6 0 1 .4 1 1 0 1.3.2 2.5.6 3.6.1.3 0 .7-.2 1z"/></svg>(+800) 555 014 2290</span>
    <span><svg width="16" height="12" viewBox="0 0 16 12"><rect width="16" height="12" rx="1" fill="#52a91d"/><path d="M1 1l7 5 7-5" stroke="#fff" fill="none" stroke-width="1.4"/></svg>contact@fenleafhelp.com</span>
  </div>
  <div class="abs search">
    <div class="field">Search for products</div>
    <div class="cat"><span>All categories</span><span>▾</span></div>
    <div class="go"><svg width="18" height="18" viewBox="0 0 20 20"><circle cx="8" cy="8" r="6" stroke="#fff" stroke-width="2.4" fill="none"/><path d="M12.5 12.5l5 5" stroke="#fff" stroke-width="2.6"/></svg></div>
  </div>
  <div class="abs minis">
    <div><svg width="12" height="11" viewBox="0 0 24 22"><path fill="#aaa" d="M12 21l-1.5-1.3C5 15 2 12 2 7.5A5 5 0 0 1 7 2.5c1.8 0 3.6.9 5 2.3a6.6 6.6 0 0 1 5-2.3 5 5 0 0 1 5 5c0 4.5-3 7.5-8.5 12.2z"/></svg>Wish List (0)</div>
    <div><svg width="12" height="11" viewBox="0 0 24 22"><path d="M2 6h17l-4-4M22 16H5l4 4" stroke="#aaa" stroke-width="2.5" fill="none"/></svg>Compare (0)</div>
  </div>
  <div class="abs cart">
    <svg width="30" height="28" viewBox="0 0 30 28"><path d="M1 3h5l4 15h15l3-10H8" stroke="#52a91d" stroke-width="2.4" fill="none"/><circle cx="12" cy="24" r="2.4" fill="#52a91d"/><circle cx="23" cy="24" r="2.4" fill="#52a91d"/><circle cx="22" cy="5" r="5" fill="#52a91d"/><text x="22" y="8" font-size="7" fill="#fff" text-anchor="middle" font-family="Open Sans, sans-serif">0</text></svg>
    <div class="label">Your Cart:<b>$0.00</b></div>
  </div>
</header>
<div class="abs rule" style="top:232px"></div>

<nav class="abs depts">
  <h3><svg width="14" height="12" viewBox="0 0 14 12"><path d="M0 1h14M0 6h14M0 11h14" stroke="#fff" stroke-width="2"/></svg>All Departments</h3>
  <ul>
    <li>Pelvarimost</li><li>Marsh hare soil tonic</li><li>Terrawix</li><li>Nuro pods</li><li>Stem triumph</li><li>Sprout charm</li><li>Vel</li><li>Flint amber</li><li>Moswelder</li>
  </ul>
</nav>

<section class="abs hero">
  <div class="kicker">WANT A</div>
  <div class="pct">20%</div>
  <div class="disc">? DISCOUNT</div>
  <div class="sub">ON NURO PODS</div>
  <div class="terms">Terms and Conditions Apply</div>
  <a class="btn">Shop Now</a>
  <div class="pack" role="img" aria-label="Open box of Nuro pods nutrient tablets with two round tablets in front"></div>
  <div class="arrow" style="left:0"><svg width="8" height="12" viewBox="0 0 8 12"><path d="M7 1L2 6l5 5" stroke="#999" stroke-width="2" fill="none"/></svg></div>
  <div class="arrow" style="right:0"><svg width="8" height="12" viewBox="0 0 8 12"><path d="M1 1l5 5-5 5" stroke="#999" stroke-width="2" fill="none"/></svg></div>
  <div class="dots"><i></i><i></i><i></i><i class="is-active"></i></div>
</section>

<div class="promo" style="left:125px">
  <h4 style="left:20px;top:34px">New Life</h4>
  <p style="left:20px;top:76px">Introducing New Category</p>
  <div class="art" role="img" aria-label="Two smartphones on a bright background" style="right:0;background:linear-gradient(120deg,#cfd8e2,#8fb0cf 50%,#6f9c4a)"></div>
</div>
<div class="promo" style="left:630px;background:linear-gradient(90deg,#d8dadd,#f1f2f3)">
  <div class="art" role="img" aria-label="Black smartwatch on a dark strap" style="left:0;background:linear-gradient(120deg,#3a3d42,#6d7278 55%,#c8cbce)"></div>
  <h4 style="right:20px;top:34px;font-style:normal">Time &amp; Style</h4>
  <p style="right:20px;top:76px">Checkout New Arrivals</p>
</div>

<div class="abs tabs"><span class="active">Featured</span><span>New Arrivals</span><span>Top Sales</span></div>
<div class="row" style="left:125px;top:960px;width:986px;height:388px">
  <div class="card" style="width:247px">
    <div class="badges"><span class="badge sale">SALE</span><span class="badge best">BESTSELLER</span></div>
    <div class="thumb" role="img" aria-label="White bottle of enzyme cleaner" style="width:70px;height:140px;background:linear-gradient(#d9d9d9,#f5f5f5 30%,#c7a76a)"></div>
    <a class="pname">Kelvra Enzyme Clear 1L</a>
    <p class="brand">Kelvra Enzymes</p>
    <div class="stars">★★★★<i>★</i></div>
    <div class="price" style="margin-top:22px"><s>$122.00</s><b>$98.00</b></div>
    <a class="addcart">Add To Cart</a>
    <div class="acts"><span>✉ Add To Wishlist</span><span>♥ Compare</span></div>
  </div>
  <div class="card" style="width:247px">
    <div class="badges"><span class="badge sale">SALE</span></div>
    <div class="thumb" role="img" aria-label="Green tub of soil pellets" style="width:110px;height:140px;background:linear-gradient(#1e7a3a,#3ea55a 60%,#1a5e2c)"></div>
    <a class="pname">Vel Soil Pellets 4.5kg</a>
    <p class="brand">Vel</p>
    <div class="stars">★★★★★</div>
    <div class="price"><b>$122.00</b></div>
  </div>
  <div class="card" style="width:247px">
    <div class="badges"><span class="badge sale">SALE</span></div>
    <div class="thumb" role="img" aria-label="Orange nutrient bottle" style="width:60px;height:140px;background:linear-gradient(#2b2b2b,#e0561b 30%,#c0400f)"></div>
    <a class="pname">Orrin Vigour 250ml</a>
    <p class="brand">Orrin</p>
    <div class="stars">★★★<i>★★</i></div>
    <div class="price"><s>$122.00</s><b>$110.00</b></div>
  </div>
  <div class="card" style="width:245px">
    <div class="badges"><span class="badge new">NEW</span></div>
    <div class="thumb" role="img" aria-label="Bag of fibre growing pots beside a fibre brick" style="width:150px;height:140px;background:linear-gradient(90deg,#e8e8e8,#f7f7f7 50%,#8a5a34)"></div>
    <a class="pname">Pottle Fibre Pot 9</a>
    <p class="brand">Pottle</p>
    <div class="stars">★★★★<i>★</i></div>
    <div class="price"><b>$1,202.00</b></div>
  </div>
</div>

<div class="abs band" style="top:1368px;height:660px"></div>
<h2 class="abs sec-title" style="left:125px;top:1403px">Best Sellers</h2>
<div class="abs grid">
  <div class="cell">
    <div class="thumb" role="img" aria-label="Two white nutrient jugs" style="width:110px;height:100px;background:linear-gradient(#eee,#fff 40%,#d84a2a)"></div>
    <a class="pname">Halden Coir Blend</a><p class="brand">Saltbreeze</p><div class="stars">★★★★★</div>
    <div class="price"><b>$122.00</b></div>
  </div>
  <div class="cell">
    <div class="thumb" role="img" aria-label="White bottle of enzyme cleaner" style="width:50px;height:100px;background:linear-gradient(#d9d9d9,#f5f5f5 30%,#c7a76a)"></div>
    <a class="pname">Kelvra Enzyme Clear</a><p class="brand">Corvale Hydroponics</p><div class="stars">★★★★★</div>
    <div class="price"><b>$337.99</b></div>
  </div>
  <div class="cell">
    <div class="thumb" role="img" aria-label="Two orange nutrient bottles" style="width:100px;height:100px;background:linear-gradient(#e36a1e,#c54d10)"></div>
    <a class="pname">CVH Mineral Mix 100g</a><p class="brand">Corvale Hydroponics</p><div class="stars">★★★★★</div>
    <div class="price"><b>$98.00</b></div>
  </div>
  <div class="cell big">
    <div class="thumb" role="img" aria-label="Wall-mounted digital water monitor with probe" style="width:300px;height:300px;background:linear-gradient(#f5f7fa,#5b8fc9 45%,#dfe6ee)"></div>
    <a class="pname" style="font-size:16px;margin-top:24px">Tarnwell Sentinel Monitor</a>
    <p class="brand" style="margin-top:8px">Corvale Hydroponics</p>
    <div class="stars">★★<i>★★★</i></div>
    <div class="price" style="border-top:0;margin-top:20px"><b style="margin-left:0;font-size:18px">$98.00</b><a class="addcart" style="margin:0;width:130px;height:40px">Add To Cart</a></div>
  </div>
  <div class="cell">
    <div class="thumb" role="img" aria-label="Black fabric grow pot" style="width:110px;height:100px;background:linear-gradient(#333,#111)"></div>
    <a class="pname">CVH Mineral Mix 100g</a><p class="brand">Corvale Hydroponics</p><div class="stars">★★★★<i>★</i></div>
    <div class="price"><b>$1,202.00</b></div>
  </div>
  <div class="cell">
    <div class="thumb" role="img" aria-label="Bag of fibre growing pots" style="width:110px;height:90px;background:linear-gradient(90deg,#e8e8e8,#f7f7f7 50%,#8a5a34)"></div>
    <a class="pname" style="margin-top:10px">CVH Mineral Mix 100g</a><p class="brand">Corvale Hydroponics</p><div class="stars">★★★★<i>★</i></div>
    <div class="price" style="margin-top:4px"><b>$122.00</b></div>
    <a class="addcart" style="width:90px;height:26px;font-size:10px;margin-top:4px">Add To Cart</a>
    <div class="acts" style="margin-top:6px;gap:10px;font-size:9px"><span>✉ Add To Wishlist</span><span>♥ Compare</span></div>
  </div>
  <div class="cell">
    <div class="thumb" role="img" aria-label="Black jerry can of root booster" style="width:80px;height:100px;background:linear-gradient(#2a2a2a,#5a8f2a 50%,#1b1b1b)"></div>
    <a class="pname">Root Rouser 4L</a><p class="brand">Corvale Hydroponics</p><div class="stars">★★★★★</div>
    <div class="price"><b>$242.00</b></div>
  </div>
</div>

<h2 class="abs sec-title" style="left:125px;top:2078px;font-size:22px">Recently Viewed</h2>
<div class="abs sec-line" style="left:300px;top:2096px;width:760px"></div>
<div class="abs navarrows" style="left:1080px;top:2082px">‹›</div>
<div class="row rv">
  <div class="card"><div class="badges"><span class="badge sale">SALE</span><span class="badge best">BESTSELLER</span></div>
    <div class="thumb" role="img" aria-label="Bag of mineral mix" style="width:70px;height:100px;background:linear-gradient(#3b2a1a,#d28a1e 60%,#4a3520)"></div>
    <a class="pname">CVH Mineral Mix 100g</a><p class="brand">Corvale Hydroponics</p><div class="stars">★★★★<i>★</i></div>
    <div class="price"><s>$122.00</s><b>$98.00</b></div></div>
  <div class="card"><div class="badges"><span class="badge best">BESTSELLER</span><span class="badge new">NEW</span></div>
    <div class="thumb" role="img" aria-label="Two orange nutrient bottles" style="width:80px;height:100px;background:linear-gradient(#e36a1e,#c54d10)"></div>
    <a class="pname">Orrin Base Duo 5L</a><p class="brand">Orrin</p><div class="stars">★★★★<i>★</i></div>
    <div class="price"><b>$122.00</b></div></div>
  <div class="card"><div class="badges"><span class="badge sale">SALE</span><span class="badge new">NEW</span></div>
    <div class="thumb" role="img" aria-label="Black bag of clay pebbles" style="width:50px;height:100px;background:linear-gradient(#222,#3a3a3a)"></div>
    <a class="pname">Clay Pebbles</a><p class="brand">Hollowmere</p><div class="stars">★★★<i>★★</i></div>
    <div class="price"><s>$122.00</s><b>$110.00</b></div></div>
  <div class="card"><div class="badges"><span class="badge new">NEW</span></div>
    <div class="thumb" role="img" aria-label="Black fabric grow pot" style="width:90px;height:100px;background:linear-gradient(#333,#111)"></div>
    <a class="pname">Loam Pot 11L</a><p class="brand">Seedwise</p><div class="stars">★★★★<i>★</i></div>
    <div class="price"><b>$1,202.00</b></div></div>
  <div class="card"><div class="badges"><span class="badge best">BESTSELLER</span><span class="badge new">NEW</span></div>
    <div class="thumb" role="img" aria-label="Black jerry can of root booster" style="width:70px;height:100px;background:linear-gradient(#2a2a2a,#5a8f2a 50%,#1b1b1b)"></div>
    <a class="pname">Root Rouser 4L</a><p class="brand">Verdan Field Nutrients</p><div class="stars">★★★★★</div>
    <div class="price"><b>$122.00</b></div></div>
  <div class="card"><div class="badges"><span class="badge best">BESTSELLER</span><span class="badge new">NEW</span></div>
    <div class="thumb" role="img" aria-label="White spray bottle of mite treatment" style="width:45px;height:100px;background:linear-gradient(#f3f3f3,#fff 40%,#d9433a)"></div>
    <a class="pname">Mitebane 250ml</a><p class="brand">Kelvra Enzymes</p><div class="stars">★★★★<i>★</i></div>
    <div class="price"><b>$122.00</b></div></div>
</div>

<h2 class="abs sec-title" style="left:125px;top:2424px;font-size:22px">Top Brands</h2>
<div class="abs sec-line" style="left:260px;top:2441px;width:800px"></div>
<div class="abs navarrows" style="left:1080px;top:2427px">‹›</div>
<div class="abs brands">
  <div><i></i>quillmarket</div><div><i></i>leafstall</div><div><i></i>leafstall</div><div><i></i>gorgecode</div><div><i></i>quillmarket</div><div><i></i>gorgecode</div>
</div>

<footer class="abs footer">
  <div class="fcol" style="left:125px">
    <h5>Featured Products</h5>
    <div class="mini"><div><a class="pname">CVH Mineral Mix 100g</a><div class="stars">★★★★★</div><div class="p"><s>$122.00</s>$98.00</div></div><div class="thumb" role="img" aria-label="Black grow pots" style="background:linear-gradient(#333,#111)"></div></div>
    <div class="mini"><div><a class="pname">CVH Mineral Mix 100g</a><div class="stars">★★★★<i>★</i></div><div class="p">$122.00</div></div><div class="thumb" role="img" aria-label="Black fabric grow pot" style="background:linear-gradient(#3a3a3a,#151515)"></div></div>
    <div class="mini"><div><a class="pname">CVH Mineral Mix 100g</a><div class="stars">★★★★<i>★</i></div><div class="p"><s>$122.00</s>$110.00</div></div><div class="thumb" role="img" aria-label="Dark nutrient bottle" style="background:linear-gradient(#222,#b5301f)"></div></div>
  </div>
  <div class="fcol" style="left:460px">
    <h5>Bestsellers Products</h5>
    <div class="mini"><div><a class="pname">CVH Mineral Mix 100g</a><div class="stars">★★★★★</div><div class="p">$122.00</div></div><div class="thumb" role="img" aria-label="Round nutrient tablet" style="background:linear-gradient(#eee,#bbb)"></div></div>
    <div class="mini"><div><a class="pname">CVH Mineral Mix 100g</a><div class="stars">★★★★★</div><div class="p">$337.99</div></div><div class="thumb" role="img" aria-label="Fibre growing pots" style="background:linear-gradient(90deg,#eee,#8a5a34)"></div></div>
    <div class="mini"><div><a class="pname">CVH Mineral Mix 100g</a><div class="stars">★★★★★</div><div class="p">$1,202.00</div></div><div class="thumb" role="img" aria-label="Round nutrient tablet" style="background:linear-gradient(#eee,#bbb)"></div></div>
  </div>
  <div class="fcol" style="left:798px">
    <h5>Latest Products</h5>
    <div class="mini"><div><a class="pname">CVH Mineral Mix 100g</a><div class="stars">★★★★★</div><div class="p">$122.00</div></div><div class="thumb" role="img" aria-label="Black grow pots" style="background:linear-gradient(#333,#111)"></div></div>
    <div class="mini"><div><a class="pname">CVH Mineral Mix 100g</a><div class="stars">★★★★<i>★</i></div><div class="p">$122.00</div></div><div class="thumb" role="img" aria-label="Black fabric grow pot" style="background:linear-gradient(#3a3a3a,#151515)"></div></div>
    <div class="mini"><div><a class="pname">CVH Mineral Mix 100g</a><div class="stars">★★★★<i>★</i></div><div class="p">$1,202.00</div></div><div class="thumb" role="img" aria-label="Black jerry can" style="background:linear-gradient(#2a2a2a,#5a8f2a)"></div></div>
  </div>

  <div class="abs sec-line" style="left:0;top:398px;width:1200px"></div>
  <div class="abs news"><div class="f">Subscribe to our newsletter</div><div class="b">Subscribe</div></div>

  <div class="abs flogo"><div class="mark"></div><div class="name">Fen Leaf Naturals</div></div>
  <div class="abs about">
    <b>Feel free to contact us via phone,email or just send us mail.</b>
    <p style="margin-top:22px">42 Alder Lane, Cambridge CB4 2XL, UK 1-888-FENLEAF (1-888-555-0147)</p>
    <b>Get in touch</b>
    <div class="social"><i></i><i></i><i></i><i></i><i></i><i></i><i></i></div>
  </div>
  <div class="links" style="left:475px"><h6>Company Information</h6>Find a store<br>Request Catalogue<br>About us<br>Contact Information<br>Customer Reviews<br>Learn</div>
  <div class="links" style="left:670px"><h6>Around Our Site</h6>Home Page<br>Grow Lights<br>Complete Grow Kits<br>Grow Tents &amp; Sheeting<br>Fans, Filters &amp; Environment<br>Growing Systems<br>Nutrients &amp; Boosters<br>Growing Media<br>Propagation<br>Grow Room Tools</div>
  <div class="links" style="left:862px"><h6>Help</h6>Quick shop<br>Track an order<br>Contact us<br>Shipping Information<br>My Account<br>Site Map</div>
</footer>

<div class="abs bottom">
  <div class="txt">Power by <b>Fen Leaf Naturals</b> © 2015</div>
  <div class="pay"><i></i><i></i><i></i><i></i></div>
</div>

</body>
</html>
```